Email signature design - law firm

We are a small boutique law firm which is located near the beach in Manly, Australia.

We have just recently developed a new logo and are looking to redesign our letterhead, business cards and email signatures.

This brief is for our email signatures. This is an email signature to appear at the bottom of our Outlook emails so we would like it to be text that we are able to edit as the wording in our email signature often required amendments.

I have attached a word document which had our new logo, and our previous email signature which all the information/wording that needs to be included.

We would like multiple designs with a modern, simplistic yet striking look.

Thanks.

font - raleway or montserrat
Updates

Colors

Designer to choose colors to be used in the design.

Requirements
Must have
• Must have the exact wording which appears in the email signature in the word document attached to brief.
• Must be able to edit the text as it is for an Outlook email signature which wording will change from time to time.

```html
<!DOCTYPE html>
<html lang="en">
<head>
<meta charset="utf-8">
<title>Email Signature – Harlow &amp; Partners</title>
<link rel="stylesheet" href="https://fonts.googleapis.com/css2?family=Montserrat:ital,wght@0,400;0,500;0,600;0,700;1,400&display=swap">
<style>
  :root {
    --navy: #2e3b87;
    --rule-blue: #7b8fcc;
    --ink: #2b2b2b;
    --text: #3a3a3a;
    --paper: #ffffff;
  }
  * { margin: 0; padding: 0; box-sizing: border-box; }
  html, body { width: 1200px; height: 515px; overflow: hidden; background: var(--paper); }
  body { font-family: "Montserrat", Arial, sans-serif; color: var(--text); }

  .signature { position: relative; width: 1200px; height: 515px; overflow: hidden; background: var(--paper); }

  .firm-mark {
    position: absolute; left: 47px; top: 200px; width: 260px;
    display: flex; align-items: center; gap: 10px;
  }
  .firm-mark__dot { width: 16px; height: 16px; border-radius: 50%; background: var(--navy); flex: none; }
  .firm-mark__name {
    font-weight: 700; font-size: 18px; color: var(--ink); letter-spacing: 0.5px; white-space: nowrap;
  }

  .contact {
    position: absolute; right: 49px; top: 40px; text-align: right;
  }
  .contact__signoff { font-size: 18px; line-height: 23px; font-weight: 400; color: var(--ink); letter-spacing: 0.3px; }
  .contact__name { margin-top: 24px; font-size: 29px; line-height: 33px; font-weight: 600; color: var(--navy); }
  .contact__list { list-style: none; margin-top: 14px; }
  .contact__item {
    display: flex; justify-content: flex-end; align-items: center; gap: 6px;
    font-size: 18px; color: var(--ink); line-height: 26px; letter-spacing: 0.2px;
  }
  .contact__item svg { width: 17px; height: 17px; fill: var(--navy); flex: none; }
  .contact__address { margin-top: 5px; font-size: 18px; line-height: 23px; color: var(--ink); letter-spacing: 0.2px; }

  .divider {
    position: absolute; left: 49px; right: 49px; top: 269px; height: 2px; background: var(--rule-blue);
  }

  .legal { position: absolute; left: 46px; right: 49px; top: 307px; }
  .legal p { font-size: 11.6px; line-height: 17px; text-align: justify; color: var(--text); }
  .legal em { color: var(--navy); font-style: italic; }
  .legal .legal__scheme {
    margin: 12px 0 11px; font-size: 12.6px; line-height: 18px; font-style: italic;
    color: var(--navy); text-align: left; letter-spacing: -0.1px;
  }

  .footer-band { position: absolute; left: 0; right: 0; bottom: 0; height: 19px; background: var(--navy); }
</style>
</head>
<body>
<div class="signature">

  <div class="firm-mark">
    <span class="firm-mark__dot"></span>
    <span class="firm-mark__name">Harlow &amp; Partners Lawyers</span>
  </div>

  <div class="contact">
    <p class="contact__signoff">Kindest regards,</p>
    <p class="contact__name">Maren Ellis</p>
    <ul class="contact__list">
      <li class="contact__item">(02) 9400 1187
        <svg viewBox="0 0 20 20" aria-hidden="true"><path d="M1 7c0-3 4-4 9-4s9 1 9 4v2h-5V7H6v2H1z"/><path d="M4 17l2-7h8l2 7z M10 11a2.5 2.5 0 1 0 0.01 0z" fill-rule="evenodd"/></svg>
      </li>
      <li class="contact__item">(02) 9400 1188
        <svg viewBox="0 0 20 20" aria-hidden="true"><rect x="5" y="2" width="10" height="5"/><path d="M1 8h18v7h-4v-3H5v3H1z"/><rect x="6" y="13" width="8" height="5"/></svg>
      </li>
      <li class="contact__item">www.harlowpartners.com.au
        <svg viewBox="0 0 20 20" aria-hidden="true"><circle cx="10" cy="10" r="9"/><path d="M1 10h18M10 1v18M3 5.5h14M3 14.5h14M10 1c-5 5-5 13 0 18M10 1c5 5 5 13 0 18" stroke="#fff" stroke-width="1.2" fill="none"/></svg>
      </li>
    </ul>
    <p class="contact__address">Suite 4, 18 Corella Lane SEAVIEW NSW 2090</p>
  </div>

  <div class="divider"></div>

  <div class="legal">
    <p><em>Important note:</em> This E-Mail and any attachment is PRIVILEGED and confidential. It must not be read, copied, disclosed or used by any personother than the above named addressees. In order to preserve the intended confidentiality and privilege, please notify us immediately if you have received this e-mail by mistake and secure-delete this e-mail from your system. Unauthorised perusal, use, disclosure, forwarding or copying is strictly prohibited and may be unlawful.</p>
    <p class="legal__scheme">Liability limited by a scheme approved under Professional Standards Legislation. Legal practitioners at CoveLaw (NSW) Pty Ltd are members of the scheme.</p>
    <p><em>Fraud warning:</em> Please be aware that there is a significant risk posed by cyber fraud, specifically relating to email accounts and bank account details. Our bank account details will never change during the course of a transaction, and we will never advise you of a change to our bank details via email. Please check account details with us in person or by phone before making payments. If you advise us of your bank account details by email, please also ring and confirm the bank account details by phone as well.</p>
  </div>

  <div class="footer-band"></div>
</div>
</body>
</html>
```